CRPG is needing business cards, and stationary created.

Pixel Forge created a logo for our business, and now we are wanting business cards, and stationary. I have included two designs of the same logo. Please feel free to use them as you want. The name of the company is Cedar Ridge Property Group LLC, the address is 812 NE Willow Ln., Suite 9, the city & state is Bend, Oregon, zip code is 97815, Telephone number is 541-327-4489, Fax number is 541-327-6051, the name on the business card is Carl Whitby CMCA

Industry/Entity Type

Property Management

Contact Information for Business Card

The card needs to look professional. Upscale.

Requirements
Must have
• The colors we are using are on the logo that has been uploaded.

```html
<!DOCTYPE html>
<html lang="en">
<head>
<meta charset="utf-8">
<title>Cedar Ridge Property Group – Business Card</title>
<link href="https://fonts.googleapis.com/css2?family=Michroma&family=Poppins:wght@400;500;600&display=swap" rel="stylesheet">
<style>
  :root {
    --teal: #138a72;
    --slate: #3d4754;
    --ink: #2f3843;
    --paper: #ffffff;
    --backdrop: #e4e6e9;
  }
  * { margin: 0; padding: 0; box-sizing: border-box; }
  html, body {
    width: 1200px; height: 672px; overflow: hidden;
    background: var(--backdrop);
  }
  .canvas {
    position: relative; width: 1200px; height: 672px;
    display: flex; align-items: center; justify-content: center;
  }
  .business-card {
    position: relative; width: 960px; height: 540px;
    background: var(--paper);
    box-shadow: 0 10px 30px rgba(0,0,0,0.15);
    overflow: hidden;
  }
  .card-frame { position: absolute; inset: 0; }
  .brand {
    position: absolute; left: 230px; top: 110px;
    display: flex; align-items: center; gap: 18px;
  }
  .brand-mark { width: 44px; height: 44px; background: var(--teal); }
  .brand-name {
    font-family: "Michroma", sans-serif; font-size: 30px;
    color: var(--teal); letter-spacing: 1px; line-height: 1.25;
    text-transform: uppercase;
  }
  .address {
    position: absolute; left: 700px; top: 118px;
    display: flex; gap: 12px;
    font-family: "Poppins", sans-serif; font-weight: 500;
    font-size: 17px; line-height: 1.35; color: var(--ink);
  }
  .address svg { flex: none; margin-top: 4px; }
  .person { position: absolute; left: 70px; top: 290px; }
  .person-name {
    font-family: "Michroma", sans-serif; font-size: 30px;
    color: var(--teal); text-transform: uppercase; letter-spacing: 1px;
  }
  .person-title {
    font-family: "Michroma", sans-serif; font-size: 24px;
    color: var(--ink); letter-spacing: 1px;
  }
  .contact-list {
    position: absolute; left: 76px; top: 380px; list-style: none;
    font-family: "Poppins", sans-serif; font-weight: 500;
    font-size: 21px; color: var(--ink); letter-spacing: 1px;
  }
  .contact-list li { display: flex; align-items: center; gap: 16px; margin-bottom: 8px; }
  .website {
    position: absolute; right: 60px; top: 410px;
    font-family: "Poppins", sans-serif; font-weight: 500;
    font-size: 22px; color: var(--paper); letter-spacing: 1px;
  }
</style>
</head>
<body>
<main class="canvas">
  <section class="business-card">
    <svg class="card-frame" width="960" height="540" viewBox="0 0 960 540">
      <path class="footer-band" d="M592 378 Q592 362 608 362 L960 362 L960 540 L560 540 L560 470 Q576 470 580 450 Z" fill="var(--slate)"/>
      <path class="accent-line" d="M0 500 L548 500 Q572 500 572 476 L572 372 Q572 346 598 346 L960 346" fill="none" stroke="var(--teal)" stroke-width="4"/>
      <rect x="0" y="504" width="960" height="36" fill="var(--paper)"/>
      <path d="M548 504 L960 504" stroke="var(--paper)" stroke-width="0"/>
    </svg>

    <div class="brand">
      <span class="brand-mark"></span>
      <span class="brand-name">Cedar Ridge<br>Property Group</span>
    </div>

    <address class="address">
      <svg width="14" height="20" viewBox="0 0 14 20" aria-hidden="true">
        <path d="M7 0C3 0 0 3 0 7c0 5 7 13 7 13s7-8 7-13c0-4-3-7-7-7zm0 10a3 3 0 110-6 3 3 0 010 6z" fill="var(--teal)"/>
      </svg>
      <span>812 NE Willow Ln.,<br>Suite 9 Bend,<br>OR 97815</span>
    </address>

    <div class="person">
      <h1 class="person-name">Carl Whitby</h1>
      <p class="person-title">CMCA</p>
    </div>

    <ul class="contact-list">
      <li>
        <svg width="22" height="18" viewBox="0 0 22 18" aria-label="Telephone">
          <path d="M1 6c0-3 4-5 10-5s10 2 10 5l-4 1-1-3c-3-1-7-1-10 0L5 7z" fill="var(--teal)"/>
          <path d="M5 9h12l3 8H2z" fill="var(--teal)"/>
        </svg>
        <span>541-327-4489</span>
      </li>
      <li>
        <svg width="22" height="20" viewBox="0 0 22 20" aria-label="Fax">
          <rect x="5" y="0" width="12" height="6" fill="var(--teal)"/>
          <rect x="0" y="7" width="22" height="9" rx="2" fill="var(--teal)"/>
          <rect x="5" y="13" width="12" height="7" fill="var(--teal)" stroke="var(--paper)" stroke-width="1.5"/>
        </svg>
        <span>541-327-6051</span>
      </li>
    </ul>

    <p class="website">www.cedarridgepg.com</p>
  </section>
</main>
</body>
</html>
```